Need 3 posters for in-store display

Hi Marlene,

Hope you are well.
I need 3 posters for display in my restaurant.

Poster 1: To be print in A1 size vertical
Title: SLURPALICIOUS DEAL $19.50
Choose any Pho OR Noodle Salads
Choose Spring Rolls (5 rolls) OR Ricepaper Rolls (2 rolls)
Choose any Cans OR Water

What I like to see:
- These poster will be place near my counter so I want it to grab customer attention.
- You must use photos to show products
- Make it easy to understand and for customer to follow

Poster 2: To be print in A4 size vertical
Title: ADD TO YOUR ORDER
SpringRolls (Crab / vegetarian) $6 / 5 rolls
Extra Meat $2
Extra Noodles $1
Extra Vegs $1.5
Extra Tofu $2
Extra Crackling $3

Poster 3: To be print in A1 size vertical
Title: BROTH BONANZA BASH
Catering Menu Options:
- PHO (Beef, Chicken, Vegan) $12.50 per bowl
- NOODLE SALADS (Beef, Chicken, BBQ Pork, Vegan) $12.50 per bowl
- SpringRolls (Crab / vegetarian) $12.50 for 10 rolls
- Ricepaper Rolls (Prawn, Beef, Chicken, BBQ Pork, Tofu) $12.5 / 5 rolls
- Fried Rice (Prawn, Tofu) $50 per tray (serve 5-6)

Terms & Conditions for All Catering Orders:
1) Minimum orders $200 (Pick-Up from shop Only)
2) All orders must be paid upfront
3) Requires $300 bond for Soup Tank
4) Please give us 48hours notice

Industry/Entity Type

Restaurant

Requirements
Nice to have
• For the SLURPALICIOUS DEAL
• it would be nice to have an image of the battle of water to visually complete the meal deal
• please see attachment of the Kestrel Ridge Water

```html
<!DOCTYPE html>
<html lang="en">
<head>
<meta charset="utf-8">
<title>Restaurant Posters</title>
<link rel="stylesheet" href="https://fonts.googleapis.com/css2?family=Anton&family=Oswald:wght@400;500;700&family=Yellowtail&display=swap">
<style>
  :root{
    --wall:#e6e7e9;
    --poster-black:#07060a;
    --poster-purple:#3a2a6a;
    --title-red:#e8262b;
    --gold:#f6c21b;
    --script-top:#fff2c4;
    --script-bottom:#f08a1c;
    --white:#ffffff;
    --rule:#4a4458;
    --food-a:#d9c7a4;
    --food-b:#7d8d4a;
    --food-c:#b6472c;
    --plate:#f4f2ee;
  }
  *{box-sizing:border-box;margin:0;padding:0}
  html,body{width:1200px;height:632px;overflow:hidden;background:var(--wall)}
  .canvas{position:relative;width:1200px;height:632px}
  .poster{
    position:absolute;overflow:hidden;color:var(--white);
    font-family:"Oswald",sans-serif;
    background:
      radial-gradient(circle at 80% 35%,rgba(110,80,180,.35) 0,transparent 22%),
      radial-gradient(circle at 20% 70%,rgba(90,70,170,.35) 0,transparent 25%),
      radial-gradient(circle at 65% 85%,rgba(120,90,200,.3) 0,transparent 20%),
      radial-gradient(ellipse at 50% 60%,var(--poster-purple) 0,var(--poster-black) 70%);
  }
  .poster--deal{left:34px;top:70px;width:356px;height:506px}
  .poster--catering{left:420px;top:70px;width:358px;height:506px}
  .poster--extras{left:809px;top:266px;width:241px;height:310px}

  .abs{position:absolute}
  .title-red{position:absolute;font-family:"Anton",sans-serif;font-weight:400;color:var(--title-red);line-height:1;letter-spacing:.5px}
  .script{
    position:absolute;font-family:"Yellowtail",cursive;line-height:1;
    background:linear-gradient(var(--script-top),var(--script-bottom));
    -webkit-background-clip:text;background-clip:text;color:transparent;
  }
  .gold{color:var(--gold)}
  .food{
    position:absolute;border-radius:50%;
    background:radial-gradient(circle at 45% 45%,var(--food-b) 0,var(--food-c) 35%,var(--food-a) 60%,var(--plate) 72%);
  }

  /* deal poster */
  .deal-title{left:20px;top:22px;font-size:38px}
  .deal-script{left:118px;top:60px;font-size:76px}
  .deal-price{position:absolute;right:24px;top:140px;font-family:"Anton",sans-serif;font-size:34px;line-height:1}
  .deal-price sup{font-size:18px;vertical-align:14px}
  .choose{position:absolute;left:20px;font-size:14px;color:var(--gold)}
  .option{position:absolute;left:20px;font-size:17px;font-weight:700;line-height:1.25}
  .option span{font-weight:400}
  .dish-label{position:absolute;font-size:8px;color:#ddd}

  /* catering poster */
  .cater-title{left:28px;top:20px;font-size:38px}
  .cater-sub{left:24px;top:74px;font-size:16px;font-weight:500;line-height:1.15}
  .cater-script{left:148px;top:62px;font-size:82px}
  .menu-row{position:absolute;left:22px;width:320px;height:60px}
  .menu-name{font-size:26px;font-weight:700;line-height:.95;text-transform:uppercase}
  .menu-name.small{font-size:22px;text-transform:none}
  .menu-note{font-size:10px;color:var(--gold)}
  .menu-price{position:absolute;right:0;top:0;text-align:center;font-family:"Anton",sans-serif;font-size:24px;color:var(--gold);line-height:1}
  .menu-price sup{font-size:13px}
  .menu-price small{display:block;font-family:"Oswald",sans-serif;font-weight:700;font-size:8px}
  .terms{position:absolute;left:22px;top:448px;width:320px;font-size:9px;color:var(--gold)}
  .terms-list{list-style:none;display:grid;grid-template-columns:1fr 1fr;gap:1px 10px;margin-top:3px;font-size:6.5px;color:#ddd}

  /* extras poster */
  .add-word{left:10px;top:18px;font-family:"Anton",sans-serif;font-weight:400;font-size:48px;color:#fff200;line-height:1}
  .add-to{left:100px;top:20px;font-size:22px;font-weight:700}
  .add-script{left:86px;top:42px;font-size:46px}
  .extras-table{position:absolute;left:28px;top:186px;width:186px;border-collapse:collapse;font-size:8px;font-weight:500}
  .extras-table td{padding:3px 0;border-bottom:1px solid var(--rule)}
  .extras-table td:last-child{text-align:right}
</style>
</head>
<body>
<main class="canvas">

  <section class="poster poster--deal" aria-label="Slurpalicious Deal poster">
    <h1 class="title-red deal-title">SLURPALICIOUS</h1>
    <div class="script deal-script">Deal</div>
    <div class="gold deal-price"><sup>$</sup>19.50</div>

    <p class="choose" style="top:186px">Choose any</p>
    <p class="option" style="top:204px">Pho OR Noodle Salads</p>

    <span class="dish-label" style="left:40px;top:232px">Beef Noodle Salad</span>
    <span class="dish-label" style="left:180px;top:228px">Chicken Noodle Salad</span>
    <span class="dish-label" style="left:296px;top:272px">Chicken Pho</span>
    <span class="dish-label" style="left:44px;top:326px">Beef Pho</span>
    <div class="food" role="img" aria-label="Photo of beef noodle salad bowl" style="left:26px;top:242px;width:96px;height:70px"></div>
    <div class="food" role="img" aria-label="Photo of chicken noodle salad bowl" style="left:126px;top:236px;width:96px;height:66px"></div>
    <div class="food" role="img" aria-label="Photo of beef pho bowl" style="left:90px;top:284px;width:100px;height:70px"></div>
    <div class="food" role="img" aria-label="Photo of chicken pho bowl" style="left:190px;top:280px;width:104px;height:74px"></div>

    <p class="choose" style="top:356px">Choose any</p>
    <p class="option" style="top:374px">Spring Rolls <span>(5 rolls)</span> OR<br>Ricepaper Rolls <span>(2 rolls)</span></p>
    <div class="food" role="img" aria-label="Photo of ricepaper rolls with dipping sauce" style="left:268px;top:356px;width:78px;height:78px;background:radial-gradient(circle,#dfe6c6 0,#a9c07a 40%,#e9e6e0 70%);border:2px solid #ccc"></div>
    <div class="food" role="img" aria-label="Photo of crispy spring rolls" style="left:202px;top:398px;width:82px;height:82px;background:radial-gradient(circle,#d58a2c 0,#b86a1c 45%,#e7e2d8 72%);border:2px solid #ccc"></div>

    <p class="choose" style="top:432px">Choose any</p>
    <p class="option" style="top:450px">Cans OR Water</p>
  </section>

  <section class="poster poster--catering" aria-label="Broth Bonanza Bash catering poster">
    <h1 class="title-red cater-title">BROTH BONANZA</h1>
    <p class="abs gold cater-sub">CATERING<br>MENU<br>OPTIONS</p>
    <div class="script cater-script">Bash</div>

    <div class="menu-row" style="top:164px">
      <p class="menu-name">Pho</p>
      <p class="menu-note">(Beef, Chicken, Vegan)</p>
      <div class="food" role="img" aria-label="Photo of two pho bowls" style="left:118px;top:-10px;width:110px;height:48px;border-radius:45%"></div>
      <p class="menu-price"><sup>$</sup>12.50<small>PER BOWL</small></p>
    </div>
    <div class="menu-row" style="top:226px">
      <p class="menu-name">Noodle<br>Salads</p>
      <p class="menu-note">(Beef, Chicken, BBQ Pork, Vegan)</p>
      <div class="food" role="img" aria-label="Photo of two noodle salad bowls" style="left:118px;top:-4px;width:110px;height:48px;border-radius:45%"></div>
      <p class="menu-price"><sup>$</sup>12.50<small>PER BOWL</small></p>
    </div>
    <div class="menu-row" style="top:304px">
      <p class="menu-name small">Spring Rolls</p>
      <p class="menu-note">(Crab / vegetarian)</p>
      <div class="food" role="img" aria-label="Photo of spring rolls with sauce" style="left:148px;top:-2px;width:80px;height:42px;border-radius:30%;background:linear-gradient(#c87a26,#e8e2d8)"></div>
      <p class="menu-price"><sup>$</sup>12.50<small>FOR 10 ROLLS</small></p>
    </div>
    <div class="menu-row" style="top:356px">
      <p class="menu-name small">Ricepaper Rolls</p>
      <p class="menu-note">(Prawn, Beef, Chicken, BBQ Pork, Tofu)</p>
      <div class="food" role="img" aria-label="Photo of ricepaper rolls" style="left:176px;top:0;width:56px;height:30px;border-radius:30%;background:linear-gradient(#e5eccd,#98b36a)"></div>
      <p class="menu-price"><sup>$</sup>12.50<small>FOR 5 ROLLS</small></p>
    </div>
    <div class="menu-row" style="top:404px">
      <p class="menu-name small">Fried Rice</p>
      <p class="menu-note">(Prawn, Tofu)</p>
      <div class="food" role="img" aria-label="Photo of fried rice tray" style="left:124px;top:-4px;width:100px;height:46px;border-radius:20%;background:radial-gradient(circle,#e2b36a 0,#c6834a 45%,#f2f0ec 72%)"></div>
      <p class="menu-price"><sup>$</sup>50<small>PER TRAY (serve 5-6)</small></p>
    </div>

    <div class="terms">
      <p>Terms &amp; Conditions for All Catering Orders:</p>
      <ol class="terms-list">
        <li>1) Minimum orders $200 (Pick-Up from shop Only)</li>
        <li>3) Requires $300 bond for Soup Tank</li>
        <li>2) All orders must be paid upfront</li>
        <li>4) Please give us 48hours notice</li>
      </ol>
    </div>
  </section>

  <section class="poster poster--extras" aria-label="Add to your order poster">
    <h1 class="abs add-word">ADD</h1>
    <p class="abs add-to">TO YOUR</p>
    <div class="script add-script">Order</div>

    <div class="food" role="img" aria-label="Photo of noodle salad bowl" style="left:6px;top:106px;width:58px;height:40px"></div>
    <div class="food" role="img" aria-label="Photo of noodle salad bowl" style="left:62px;top:100px;width:58px;height:40px"></div>
    <div class="food" role="img" aria-label="Photo of pho bowl" style="left:52px;top:132px;width:62px;height:42px"></div>
    <div class="food" role="img" aria-label="Photo of pho bowl" style="left:112px;top:128px;width:62px;height:44px"></div>
    <div class="food" role="img" aria-label="Photo of ricepaper rolls" style="left:176px;top:98px;width:38px;height:38px;background:radial-gradient(circle,#dfe6c6 0,#a9c07a 40%,#e9e6e0 70%)"></div>
    <div class="food" role="img" aria-label="Photo of spring rolls" style="left:196px;top:134px;width:40px;height:40px;background:radial-gradient(circle,#d58a2c 0,#b86a1c 45%,#e7e2d8 72%)"></div>

    <table class="extras-table">
      <tr><td>SpringRolls (Crab / vegetarian)</td><td>$6 / 5 rolls</td></tr>
      <tr><td>Extra Meat</td><td>$2</td></tr>
      <tr><td>Extra Noodles</td><td>$1</td></tr>
      <tr><td>Extra Vegs</td><td>$1.5</td></tr>
      <tr><td>Extra Tofu</td><td>$2</td></tr>
      <tr><td>Extra Crackling</td><td>$3</td></tr>
    </table>
  </section>

</main>
</body>
</html>
```